Home builder/contractor needs business presentation brochure

We are a custom home and remodeling firm who would like a great brochure to present to architects, designers, real estate brokers.

We are looking for additional avenues for growth potential and the ability to partner with the above types of businesses to give us an all around encompassing one stop shopping.

Target Market(s)

architects, designers, real estate brokers.

Industry/Entity Type

Real Estate

Requirements
Must have
• Please make this a tri fold and please checkout my website ridgemarkhomes.example and my houzz site as well as yelp. to gather additional information.

```html
<!DOCTYPE html>
<html lang="en">
<head>
<meta charset="utf-8">
<title>Ridgemark Homes – Tri-fold Brochure</title>
<link rel="stylesheet" href="https://fonts.googleapis.com/css2?family=Open+Sans:wght@400;600&family=Parisienne&display=swap">
<style>
  :root{
    --charcoal:#3a3a3c;
    --blue:#5aa6dc;
    --paper:#ffffff;
    --mist:#f1f1f1;
    --ink:#4a4a4a;
    --soft-ink:#8a8a8a;
    --stage:#e6e6e6;
  }
  *{margin:0;padding:0;box-sizing:border-box}
  html,body{width:759px;height:1200px;overflow:hidden}
  body{background:var(--stage);font-family:"Open Sans",Arial,sans-serif;position:relative}
  .sheet{position:absolute;left:37px;width:683px;height:529px;background:var(--paper);overflow:hidden}
  .sheet--outside{top:66px}
  .sheet--inside{top:637px}
  .abs{position:absolute}
  .photo{position:absolute}
  /* outside */
  .mission-panel{left:0;top:0;width:228px;height:529px;background:var(--charcoal);color:#eee}
  .heading{color:var(--blue);font-size:13px;font-weight:400}
  .mission-panel .heading{position:absolute;left:12px;top:25px}
  .mission-text{position:absolute;left:10px;top:50px;width:210px;font-size:8.2px;line-height:1.38;text-align:justify;color:#f0f0f0}
  .caption{position:absolute;left:0;width:228px;top:358px;text-align:center;font-size:11px;color:var(--blue)}
  .contractor{position:absolute;left:91px;top:417px;font-size:7.6px;line-height:1.45;color:#eee}
  .contractor p+p{margin-top:13px}
  .testimonials{left:228px;top:0;width:225px;height:499px;background:#fbfbfb}
  .quote{position:absolute;left:24px;width:184px;font-size:8.2px;line-height:1.33;color:var(--ink);text-align:justify}
  .quote cite{display:block;font-style:normal;text-align:left}
  .call{position:absolute;left:0;width:225px;top:428px;text-align:center;font-size:8.6px;line-height:1.4;color:#222}
  .web-bar{left:0;top:499px;width:453px;height:13px;background:var(--blue)}
  .web-bar span{position:absolute;left:228px;width:225px;text-align:center;top:-2px;font-size:11.5px;color:#222}
  .cover{left:453px;top:0;width:120px;height:529px;background:var(--mist)}
  .brand{position:absolute;left:0;width:120px;top:72px;text-align:center;font-size:9.5px;color:#5f6b78;letter-spacing:.5px}
  .brand-mark{display:block;width:34px;height:34px;margin:0 auto 8px;background:var(--blue)}
  .tagline{position:absolute;right:12px;top:188px;width:100px;text-align:right;font-family:"Parisienne",cursive;font-size:15px;line-height:1.5;color:#b9b9b9}
  .services{position:absolute;right:10px;top:365px;width:110px;text-align:right;font-size:11px;line-height:1.35;color:var(--soft-ink)}
  .social{position:absolute;left:15px;top:494px;display:flex;gap:4px}
  .social i{display:block;width:17px;height:17px;background:#9a9a9a}
  /* inside */
  .info-panel{left:0;top:0;width:228px;height:503px;background:var(--paper)}
  .info-panel .heading{position:absolute;left:10px;font-size:11px}
  .info-text{position:absolute;left:10px;width:212px;font-size:7.8px;line-height:1.4;color:#333}
  .gallery{left:228px;top:0;width:455px;height:503px;background:var(--charcoal)}
  .base-bar{left:0;top:503px;width:683px;height:13px;background:var(--blue)}
  .base-strip{left:228px;top:516px;width:455px;height:13px;background:var(--charcoal)}
</style>
</head>
<body>

<section class="sheet sheet--outside">
  <div class="abs mission-panel">
    <h2 class="heading">Our Mission</h2>
    <p class="mission-text">&nbsp;To build every project as if we were building it for ourselves. Contractor Dan Whitaker has over 34 years experience and his eye for the smallest detail sets him apart as one of the best contractors in the Bay Area. Rest assure Dan will handle your home project from start to finish; his great ideas and sound advice gives each individual project he works on the uniqueness that will reflect and surpass every homeowners dream.</p>
    <div class="photo" style="left:0;top:178px;width:228px;height:174px;background:linear-gradient(180deg,#8fb7de 0%,#c9b79a 45%,#6f8a4a 100%)" role="img" aria-label="Mediterranean-style two-storey home with landscaped driveway"></div>
    <p class="caption">Beautiful homes built to last</p>
    <div class="photo" style="left:0;top:392px;width:87px;height:96px;background:linear-gradient(180deg,#9a7a5c,#6d5a48)" role="img" aria-label="Portrait of the general contractor"></div>
    <div class="contractor">
      <p>General Contractor:<br>Dan Whitaker</p>
      <p>Location: 1840 Alder Crest Lane<br>San Mateo, CA 94403<br>License Number: 482915</p>
    </div>
  </div>

  <div class="abs testimonials">
    <div class="quote" style="top:4px">“Dan took on our project when other contractors didn't want to. His crew worked 6 days a week to get our house completed for our family. Plus, Dan has an eye for design and gave us some great ideas. Dan has a lot of integrity and does what he says he will do. He stands behind his work.”<cite>— Carla Hensley (Belmont, CA)</cite></div>
    <div class="quote" style="top:125px">“Dan is truly a fine home builder who is passionate about his work. He is trustworthy, creative, and has an amazing eye for detail. His standards are extremely high, and he expects the same from his employees and subcontractors. My sincere thanks.”<cite>— Mira Calloway (Menlo Park, CA)</cite></div>
    <div class="quote" style="top:226px">“Ridgemark Homes is the best contractor that I ever worked with. They remodeled and built the additional rooms to our house in Hillsborough. Dan Whitaker, the owner, is a trustworthy, honest and responsible contractor and provides high caliber work. He was adamant about the quality of the work and managed his crew closely, making sure that we had perfectly finished work. From Day 1 interviewing him for the project through completion, we had no regrets picking him. He is so talented that he gave us ideas on the design, color and furniture. Not only that, the cost of the project was very close to the estimate that he provided. We are so happy with his work and have become good friends with Dan. We will definitely use him on our next project.”<cite>— Grace Lindqvist (Hillsborough, CA)</cite></div>
    <p class="call">Call us at 650-555-0142<br>or email us at dan@ridgemarkhomes.example<br>for a free consultation on your<br>construction project.</p>
  </div>

  <div class="abs web-bar"><span>www.ridgemarkhomes.example</span></div>

  <div class="abs cover">
    <p class="brand"><span class="brand-mark"></span>RIDGEMARK HOMES</p>
    <p class="tagline">Beautiful<br>Homes - Built<br>To Last</p>
    <p class="services">Expert home construction, remodeling and additions in San Mateo County</p>
    <div class="social"><i></i><i></i><i></i></div>
  </div>

  <div class="photo" style="left:573px;top:0;width:110px;height:529px;background:linear-gradient(180deg,#6a5a48 0%,#3b2f26 40%,#b7a58d 75%,#d8cbb7 100%)" role="img" aria-label="Arched wrought-iron entry doors with lantern and stone steps"></div>
</section>

<section class="sheet sheet--inside">
  <div class="abs info-panel">
    <h2 class="heading" style="top:17px">About us</h2>
    <p class="info-text" style="top:35px">When it comes building or remodeling your home, only the best will do. Superior quality home construction happens with experts guiding the building process.<br>With over 34 years of building experience, General Contractor Dan Whitaker of Ridgemark Homes in San Mateo has a well-earned reputation of helping homeowners realize their dream home.</p>
    <div class="photo" style="left:0;top:123px;width:228px;height:112px;background:linear-gradient(180deg,#a9c3dc 0%,#d9d2c0 45%,#5f8a3e 100%)" role="img" aria-label="Large colonial-style home with columns and lawn"></div>
    <h2 class="heading" style="top:243px">Quality, Reliability, Value</h2>
    <p class="info-text" style="top:261px">At Ridgemark Homes we insist on quality building materials and superb craftsmanship with long-term performance and value utmost in our minds. Our #1 priority is to deliver superior service and continually maintain customer satisfaction. Realizing this standard of quality and value is only accomplished by being highly selective of every product and component that goes into building your home. This uncompromising standard in quality construction is why you can trust Ridgemark Homes when building or remodeling your home.</p>
    <div class="photo" style="left:0;top:380px;width:228px;height:117px;background:linear-gradient(180deg,#9cc0e2 0%,#c8d6e2 50%,#8a6a55 80%,#e8e4dc 100%)" role="img" aria-label="Pergola terrace overlooking a lake"></div>
  </div>

  <div class="abs gallery">
    <div class="photo" style="left:1px;top:1px;width:294px;height:194px;background:linear-gradient(160deg,#f1efe9 0%,#d9d3c8 55%,#8f8578 100%)" role="img" aria-label="White kitchen with granite counters"></div>
    <div class="photo" style="left:1px;top:201px;width:144px;height:97px;background:linear-gradient(180deg,#7b5a3e,#a98a6a)" role="img" aria-label="Outdoor kitchen under a wooden pergola"></div>
    <div class="photo" style="left:154px;top:201px;width:141px;height:97px;background:linear-gradient(180deg,#3d3d3d,#e9e9e9 60%,#2a2a2a)" role="img" aria-label="Modern bathroom with trough sink"></div>
    <div class="photo" style="left:303px;top:1px;width:152px;height:295px;background:linear-gradient(180deg,#9ec4e6 0%,#d8c7ad 40%,#a0683c 70%,#cfcac0 100%)" role="img" aria-label="Modern home entry with wood siding and steps"></div>
    <div class="photo" style="left:1px;top:304px;width:144px;height:199px;background:linear-gradient(180deg,#d6cdbc,#b8ac96 60%,#ece8e0)" role="img" aria-label="Tiled walk-in shower with glass door"></div>
    <div class="photo" style="left:154px;top:304px;width:301px;height:199px;background:linear-gradient(180deg,#c9a77f 0%,#8a5e3a 55%,#5b3c24 100%)" role="img" aria-label="Wood-cabinet kitchen with island and pendant lights"></div>
  </div>

  <div class="abs base-bar"></div>
  <div class="abs base-strip"></div>
</section>

</body>
</html>
```